Can you make FairlyKind look better than average? We need business cards and a logo refresh :-)

REVISED BRIEF

PRIORITY

VECTOR LOGO

Create a vector version of our existing logo. The logo must not change from its current design, weight or font.

Deliverables

- Logo in blue (#2540BB)
- Logo in white (#FFFFFF)
- Logo in grey (#36454F)
- All logos on transparent background
- All logos in PNG & SVG formats. (SVG must NOT distort stroke width when resized)

BRAND MARK

Create a brand mark for use with the logo. This should be possible to used with the logo and on its own as a stand alone graphical device that represents the FAIRLYKIND brand.

https://sitecrafter.example.com/resources/glossary/what-is-a-brand-mark

Deliverables

- Brand Mark in blue (#2540BB)
- Brand Mark in white (#FFFFFF)
- Brand Mark in grey (#36454F)
- Brand Mark on transparent background
- Brand Mark in PNG & SVG formats. (SVG must NOT distort stroke width when resized)
- Logo combined with Brand Mark (colours and formats)
.

Business Card Layout

Create 2 layouts with the following details:-

Marcus Trent
Co-Founder & Chief Product Officer

marcus@fairlykind.example.nz
www.fairlykind.example.nz
0279816354

Callum Bryce
Founder & CEO

hello@fairlykind.example.nz
www.fairlykind.example.nz
021 948 6207

DESIGN CONSIDERATIONS

Create versions with ‘Shaping Names With Heart’ tag line incorporated within the design and without (maintain separation of logo from tag line)

- Create a version with and without the brand mark
- Keep it clean and simple but elevate the design with subtle design effects
- Consider use of raised spot gloss colour (this can be white on white for subtle or blue on blue or blue on white)
- Consider use of spot gloss colour (this can be white on white for subtle or blue on blue or blue on white)
- Consider use of letterpress indentation
- Ensure contact details are legible, use sans-serif font

PREVIOUS BRIEF

We need a business card design for our business FairlyKind. We are a purpose driven brand and media agency that helps brands and charities plan and buy traditional media campaigns (TV, Radio, Print, Outdoor etc). We give a significant amount of the media booking fees we receive from media vendors to charity in the name of our clients. https://www.socialnet.example.com/posts/wearefairlykind_giveback-fairlykind-shapingnameswithheart-activity-5820394716253849102-Xqzt

Our strapline is 'Shaping Names With Heart'.

We want to keep our logo design as it is but it does need tightening up and made into a proper vector image as it's been created from a font.

Our brand colour is #2540BB and we need to keep this.

Our brand is professional but human, warm and engaging and doesn't take itself too seriously.

Things We Need
- vectorisation and tidying up of existing logo
- We'd like you to think about how we can incorporate a brand mark with the logo to add another dimension to our brand
- business card layout and design
- we'll be using cardloop.example.com to print the cards so please take a look at the options they have (spot gloss, foil, letterpress, square cards and even the backs of the cards can have a different design on every single card!
- potential opportunity for different famous quotes on the back or imagery or slight design differences
- we'd be open to the use of an emoji or emojiis as the brandmark or to be incorporated into the card designs
- we can have as many different design batches as we like for the backs of the cards

https://www.cardloop.example.com/au/business-cards

We want to make an impact, we want to be seen as professional but fun, we want to be different.

Here's a press release of what we're about.

https://adwirenews.example.co.nz/movings-shakings/fairlykind-welcomes-marcus-trent-as-co-founder/

Be bold, be different, there is no such thing as a bad idea. We're open to anything so please bring your best ideas and have fun with it! Go crazy if you like!
____________
Marcus Trent
marcus@fairlykind.example.nz
0279816354

Callum Bryce
Founder & CEO
hello@fairlykind.example.nz
021 948 6207

Shaping Names With Heart

________

These are the only details we MUST have on the cards, the rest is up to you. Just make sure you use all of your creativity but don't feel the need to crowd the card with too much, let it breathe as well.

In terms of font for the details, we'll leave that up to you, just ensure it's legible. Oh and please don't take any design inspiration from our website - that will be changing!

Please don't let the design and layout look cheap and tacky though. It needs to still feel premium but personable.

Thanks

Marcus
Updates

Many designs are changing the logo and this was NOT in the brief. We need a brand mark to complement the logo. We need to see the logo with and without the brand mark. We need to see the business card with both logo + brand mark and logo on its own We need to see the business card with and without the tagline 'Shaping Names With Heart'

Industry/Entity Type

purpose driven Brand & Media Agency

Contact Information for Business Card

Shaping Names With Heart
Marcus Trent, Co-Founder & Chief Product Officer, marcus@fairlykind.example.nz fairlykimd.example.nz, 0279 816 354

Callum Bryce, Founder & CEO hello@fairlykind.example.nz, fairlykimd.example.nz, 021 948 6207

Font styles to use
Serif
Sans Serif

Colors
0054AA
0677BA
7BADD7
CADEEF
E8F1F8

Requirements
Must have
• brand mark, vector version of existing logo, Shaping Names With Heart tagline, existing logo traced and vectorised. Must fully explore the design options from cardloop.example.com that can enhance the overall card design
Nice to have
• brandmark to help elevate the logo, maybe incorporate some other design elements into the card like lines, or grids.
Should not have
• A cheap look and feel

```html
<!DOCTYPE html>
<html lang="en">
<head>
<meta charset="utf-8">
<title>FairlyKind – Business Cards</title>
<link href="https://fonts.googleapis.com/css2?family=Roboto:wght@300;400;500;900&display=swap" rel="stylesheet">
<style>
  :root {
    --stage: #e6e7e9;
    --brand: #3a4ea2;
    --ink: #36454f;
    --muted: #4a5560;
    --rule: #8a93cc;
    --paper: #ffffff;
  }
  * { margin: 0; padding: 0; box-sizing: border-box; }
  html, body { width: 1200px; height: 847px; overflow: hidden; }
  body {
    position: relative;
    background: var(--stage);
    font-family: "Roboto", sans-serif;
    color: var(--ink);
  }
  .sheet-title {
    position: absolute; left: 102px; top: 52px;
    font-size: 23px; font-weight: 400; letter-spacing: 0.2px;
    color: var(--brand);
  }
  .card {
    position: absolute; width: 501px; height: 286px;
    background: var(--paper);
    box-shadow: 3px 4px 9px rgba(0,0,0,0.16);
  }
  .card--front-a { left: 101px; top: 113px; }
  .card--front-b { left: 628px; top: 115px; }
  .card--back-white { left: 101px; top: 452px; }
  .card--back-blue { left: 628px; top: 454px; background: var(--brand); }

  .wordmark {
    font-family: "Roboto", sans-serif; font-weight: 900;
    letter-spacing: 0.3px; line-height: 1; white-space: nowrap;
  }
  .card__logo { position: absolute; left: 32px; top: 35px; font-size: 22px; color: var(--brand); }
  .card__logo--centered {
    position: absolute; left: 0; right: 0; top: 50%; transform: translateY(-50%);
    text-align: center; font-size: 35px;
  }
  .card--back-white .card__logo--centered { color: var(--ink); }
  .card--back-blue .card__logo--centered { color: #fff; }

  .accent-bar { position: absolute; left: 0; top: 152px; width: 10px; height: 27px; background: var(--brand); }
  .person { position: absolute; left: 33px; top: 148px; }
  .person__name { font-size: 19px; font-weight: 500; line-height: 1.1; color: var(--ink); }
  .person__first { color: var(--brand); }
  .person__role { font-size: 10.5px; font-weight: 300; color: var(--muted); margin-top: 1px; }
  .divider { position: absolute; right: 0; top: 180px; height: 1px; background: var(--rule); }
  .card--front-a .divider { left: 125px; }
  .card--front-b .divider { left: 229px; }

  .contacts { position: absolute; left: 33px; list-style: none; }
  .card--front-a .contacts { top: 215px; }
  .card--front-b .contacts { top: 218px; }
  .contacts li {
    display: flex; align-items: center; height: 14.5px;
    font-size: 11.5px; font-weight: 300; color: var(--muted);
  }
  .contacts svg { width: 9px; height: 9px; margin-right: 14px; fill: var(--brand); flex: none; }
</style>
</head>
<body>
  <h1 class="sheet-title">ALL LOGOS IN PNG &amp; SVG FORMATS</h1>

  <section class="card card--front-a">
    <div class="card__logo wordmark">FAIRLYKIND</div>
    <span class="accent-bar"></span>
    <div class="person">
      <p class="person__name"><span class="person__first">Callum</span> Bryce</p>
      <p class="person__role">Founder &amp; CEO2</p>
    </div>
    <span class="divider"></span>
    <ul class="contacts">
      <li><svg viewBox="0 0 10 10"><path d="M2 0.5l2 2-1 1.2c.6 1.3 1.5 2.2 2.8 2.8l1.2-1 2 2-1.3 1.8C4 9 1 6 0.2 1.8z"/></svg>021 948 6207</li>
      <li><svg viewBox="0 0 10 10"><path d="M0.5 2h9v6h-9z M0.5 2l4.5 3.3 4.5-3.3" stroke="#fff" stroke-width="0.8"/></svg>hello@fairlykind.example.nz</li>
      <li><svg viewBox="0 0 10 10"><circle cx="5" cy="5" r="4.6"/><path d="M2.2 3.2h2.4v2H2.8zM5.6 5.6h2v2.2H6z" fill="#fff"/></svg>www.fairlykind.example.nz</li>
    </ul>
  </section>

  <section class="card card--front-b">
    <div class="card__logo wordmark">FAIRLYKIND</div>
    <span class="accent-bar"></span>
    <div class="person">
      <p class="person__name"><span class="person__first">Marcus</span> Trent</p>
      <p class="person__role">Co-Founder &amp; Chief Product Officer</p>
    </div>
    <span class="divider"></span>
    <ul class="contacts">
      <li><svg viewBox="0 0 10 10"><path d="M2 0.5l2 2-1 1.2c.6 1.3 1.5 2.2 2.8 2.8l1.2-1 2 2-1.3 1.8C4 9 1 6 0.2 1.8z"/></svg>0279816354</li>
      <li><svg viewBox="0 0 10 10"><path d="M0.5 2h9v6h-9z M0.5 2l4.5 3.3 4.5-3.3" stroke="#fff" stroke-width="0.8"/></svg>marcus@fairlykind.example.nz</li>
      <li><svg viewBox="0 0 10 10"><circle cx="5" cy="5" r="4.6"/><path d="M2.2 3.2h2.4v2H2.8zM5.6 5.6h2v2.2H6z" fill="#fff"/></svg>www.fairlykind.example.nz</li>
    </ul>
  </section>

  <section class="card card--back-white">
    <div class="card__logo--centered wordmark">FAIRLYKIND</div>
  </section>

  <section class="card card--back-blue">
    <div class="card__logo--centered wordmark">FAIRLYKIND</div>
  </section>
</body>
</html>
```